Beauty and cosmetics line, need a new design for my upcoming collection

I need someone to create and new design for my upcoming collection that suits the look and feel of my brand. My brand is woman owned and is called Vurano Cosmetics based in the UAE. It is a start up business and I am keen to establish myself in the beauty industry. My color palette is very neutral and is consisted of nudes and shades of brown, this upcoming collection will be a big one so I need it to be perfect, to stand out and to be unforgettable. The products are liquid lipsticks, concealer and foundation, the collection name is "Vurano Essentials"

Target Market(s)

makeup and beauty enthusiasts, makeup artists, general public

Colors

Designer to choose colors to be used in the design.

Requirements
Must have
• authentic identity

```html
<!DOCTYPE html>
<html lang="en">
<head>
<meta charset="utf-8">
<title>Vurano Essentials – Liquid Lipstick Carton Dieline</title>
<link rel="stylesheet" href="https://fonts.googleapis.com/css2?family=Poppins:wght@400;500;600&display=swap">
<style>
  :root {
    --paper: #ffffff;
    --nude-light: #fde9d8;
    --nude-mid: #fdd9b4;
    --nude-deep: #fdc990;
    --bronze: #8b6a3b;
    --bronze-soft: #9a7a4c;
    --cut-line: #2e2a26;
    --pattern-tint: #e8cdb2;
    --pattern-white: #ffffff;
  }
  html, body {
    margin: 0;
    padding: 0;
    width: 1111px;
    height: 1200px;
    overflow: hidden;
    background: var(--paper);
  }
  .dieline {
    display: block;
    width: 1111px;
    height: 1200px;
  }
  .cut { stroke: var(--cut-line); stroke-width: 1; }
  .panel-fill { fill: url(#carton-gradient); }
  .flap-top { fill: var(--nude-light); }
  .flap-bottom { fill: var(--nude-deep); }
  .brand-text {
    font-family: "Poppins", sans-serif;
    font-weight: 600;
    fill: var(--bronze);
  }
  .brand-name { font-size: 80px; letter-spacing: -1px; }
  .brand-collection { font-size: 32px; letter-spacing: 3px; }
  .side-name { font-size: 50px; letter-spacing: -1px; }
  .side-collection { font-size: 22px; letter-spacing: 2px; }
  .product-type {
    font-family: "Poppins", sans-serif;
    font-weight: 400;
    font-size: 15px;
    letter-spacing: 1px;
    fill: var(--bronze-soft);
  }
  .web-address {
    font-family: "Poppins", sans-serif;
    font-weight: 400;
    font-size: 22px;
    fill: var(--bronze);
  }
  .spec-text {
    font-family: "Poppins", sans-serif;
    font-weight: 400;
    font-size: 11px;
    fill: var(--bronze);
  }
  .body-copy {
    font-family: "Poppins", sans-serif;
    font-weight: 400;
    font-size: 11.2px;
    fill: var(--bronze);
  }
  .tuck-name {
    font-family: "Poppins", sans-serif;
    font-weight: 600;
    font-size: 15px;
    letter-spacing: 2px;
    fill: var(--bronze);
  }
  .icon-stroke { fill: none; stroke: var(--bronze); stroke-width: 1.4; }
  .pattern-faint { fill: var(--pattern-tint); opacity: 0.35; }
  .pattern-light { fill: var(--pattern-white); opacity: 0.3; }
</style>
</head>
<body>
<svg class="dieline" viewBox="0 0 1000 1080" xmlns="http://www.w3.org/2000/svg">
  <defs>
    <linearGradient id="carton-gradient" x1="0" y1="0" x2="0" y2="1">
      <stop offset="0" stop-color="var(--nude-light)"/>
      <stop offset="0.5" stop-color="var(--nude-mid)"/>
      <stop offset="1" stop-color="var(--nude-deep)"/>
    </linearGradient>
  </defs>

  <!-- top flaps -->
  <g class="top-flaps">
    <path class="flap-top cut" d="M243 207 L258 165 L338 165 L353 207 Z"/>
    <path class="flap-top cut" d="M353 207 L353 95 L370 53 L446 53 L463 95 L463 207 Z"/>
    <line class="cut" x1="353" y1="95" x2="463" y2="95"/>
    <path class="flap-top cut" d="M463 207 L478 165 L556 165 L571 207 Z"/>
  </g>

  <!-- tuck flap name -->
  <g class="tuck-brand">
    <rect x="390" y="144" width="8" height="8" fill="var(--bronze)"/>
    <text class="tuck-name" x="404" y="153">VURANO</text>
  </g>

  <!-- bottom flaps -->
  <g class="bottom-flaps">
    <path class="flap-bottom cut" d="M243 885 L258 925 L338 925 L353 885 Z"/>
    <path class="flap-bottom cut" d="M353 885 L353 995 L370 1027 L446 1027 L463 995 L463 885 Z"/>
    <line class="cut" x1="353" y1="995" x2="463" y2="995"/>
    <path class="flap-bottom cut" d="M463 885 L478 925 L556 925 L571 885 Z"/>
  </g>

  <!-- main panels -->
  <g class="panels">
    <rect class="panel-fill cut" x="243" y="207" width="110" height="678"/>
    <rect class="panel-fill cut" x="353" y="207" width="110" height="678"/>
    <rect class="panel-fill cut" x="463" y="207" width="108" height="678"/>
    <rect class="panel-fill cut" x="571" y="207" width="109" height="678"/>
    <path class="panel-fill cut" d="M680 207 L718 250 L718 840 L680 885 Z"/>
  </g>

  <!-- decorative pattern areas -->
  <rect class="pattern-faint" x="265" y="210" width="330" height="140" role="img" aria-label="Faint interlocking circle pattern across the upper panels"/>
  <rect class="pattern-light" x="466" y="690" width="210" height="192" role="img" aria-label="Light interlocking circle pattern at the foot of the side panels"/>

  <!-- panel 1: description copy -->
  <text class="body-copy" transform="translate(272 862) rotate(-90)">
    <tspan x="0" y="0">Lorem Ipsum is simply dummy text of the printing and typesetting industry. Lorem Ipsum</tspan>
    <tspan x="0" y="14.5">has been the industry's standard dummy text ever since the 1500s, when an unknow</tspan>
    <tspan x="0" y="29">printer took a galley of type and scrambled it to make a type specimen book.</tspan>
  </text>

  <!-- panel 2: front brand -->
  <text class="brand-text" transform="translate(462 882) rotate(-90)">
    <tspan class="brand-name">VURANO</tspan><tspan class="brand-collection" dx="14">ESSENTIALS</tspan>
  </text>

  <!-- panel 3: details -->
  <text class="web-address" transform="translate(521 812) rotate(-90)">www.vuranocosmetics.com</text>
  <text class="spec-text" transform="translate(540 328) rotate(-90)">Made in PRC</text>
  <text class="spec-text" transform="translate(555 412) rotate(-90)">Net WT. 5.0 gr / 0.18 oz e</text>

  <g class="info-icons">
    <!-- period after opening -->
    <g transform="translate(512 325) rotate(-90)">
      <rect class="icon-stroke" x="-12" y="-7" width="24" height="14" rx="2"/>
      <text class="spec-text" x="-8" y="4" style="font-size:8px">12M</text>
    </g>
    <!-- recycling -->
    <g transform="translate(505 285)">
      <path class="icon-stroke" d="M-8 4 A9 9 0 0 1 -2 -8"/>
      <path class="icon-stroke" d="M2 -8 A9 9 0 0 1 8 4"/>
      <path class="icon-stroke" d="M6 8 A9 9 0 0 1 -6 8"/>
      <path d="M-4 -11 L1 -8 L-4 -5 Z M10 1 L8 7 L4 2 Z M-9 10 L-7 4 L-3 9 Z" fill="var(--bronze)"/>
    </g>
    <!-- certification badge -->
    <circle class="icon-stroke" cx="522" cy="244" r="12" role="img" aria-label="Certification badge"/>
  </g>

  <!-- panel 4: side brand -->
  <text class="brand-text" transform="translate(634 826) rotate(-90)">
    <tspan class="side-name">VURANO</tspan><tspan class="side-collection" dx="14">ESSENTIALS</tspan>
  </text>
  <text class="product-type" transform="translate(630 432) rotate(-90)">LIQUID LIPSTICK</text>
</svg>
</body>
</html>
```